Brett Olsen Building Business Card Design

Hi,

I need a business card for my Building company.
I am a Builder and build homes for clients.
I am looking for a sophisticated logo that can be used on business cards, envelopes and letter heads.
I am trying to take my business to the next level and need a professional business card.

Colours: Please use white, black, dark grey and bright blue.

Thank you,

Carol and Brett.

Target Market(s)

1. Home and Building Companies 2. Potential customers

Industry/Entity Type

Business

Contact Information for Business Card

Brett Olsen Building PTY LTD

Brett Olsen

Director

A.B.N. 37 829 516 073

BUILDERS LICENCE No. 573019k

Mobile: 0412 907 381

Email: brettolsenbuilding@mailvane.com.au

Requirements
Must have
• The following is compulsory to have in the designs:

Brett Olsen Building PTY LTD (business name)

Brett Olsen (contact name)

Director (position)

A.B.N. 37 829 516 073

Builders Licence No. 573019k

Mobile: 0412 907 381

Nice to have
• Logo for business
Should not have
• Should not be cluttered.

I am looking for a clean, sophisticated and professional business card design.

```html
<!DOCTYPE html>
<html lang="en">
<head>
<meta charset="utf-8">
<title>Brett Olsen Building – Business Card</title>
<link rel="stylesheet" href="https://fonts.googleapis.com/css2?family=EB+Garamond:wght@400;500&display=swap">
<style>
  :root {
    --navy: #1e2160;
    --ink: #1b1c45;
    --bg-light: #f6f6f6;
    --bg-mid: #d9d9d9;
    --bg-dark: #9e9e9e;
    --divider-light: #ffffff;
    --divider-dark: #8c8c8c;
  }
  html, body {
    margin: 0;
    padding: 0;
    width: 1200px;
    height: 730px;
    overflow: hidden;
  }
  .card {
    position: relative;
    width: 1200px;
    height: 730px;
    background:
      radial-gradient(ellipse 75% 90% at 40% 48%, var(--bg-light) 0%, var(--bg-mid) 55%, var(--bg-dark) 100%);
    font-family: "EB Garamond", Georgia, serif;
    color: var(--ink);
  }
  .divider {
    position: absolute;
    left: 598px;
    top: 30px;
    width: 6px;
    height: 670px;
    background: linear-gradient(to bottom, transparent 0%, var(--divider-dark) 20%, var(--divider-dark) 80%, transparent 100%);
    box-shadow: 4px 0 6px rgba(255,255,255,0.8), -2px 0 6px rgba(0,0,0,0.12);
    opacity: 0.85;
  }
  .divider::after {
    content: "";
    position: absolute;
    left: 4px;
    top: 0;
    width: 3px;
    height: 100%;
    background: linear-gradient(to bottom, transparent 0%, var(--divider-light) 25%, var(--divider-light) 75%, transparent 100%);
  }
  .brand {
    position: absolute;
    left: 0;
    width: 600px;
    top: 318px;
    text-align: center;
  }
  .brand-name {
    font-size: 44px;
    font-weight: 500;
    color: var(--navy);
    line-height: 1;
    margin: 0;
  }
  .brand-legal {
    margin-top: 52px;
    font-size: 22px;
    line-height: 26px;
    color: var(--ink);
  }
  .contact {
    position: absolute;
    left: 702px;
    top: 200px;
  }
  .contact-name {
    margin: 0;
    font-size: 44px;
    font-weight: 500;
    color: var(--navy);
    line-height: 1;
    display: inline-block;
    padding: 0 2px 4px 0;
    border-bottom: 3px solid var(--navy);
  }
  .contact-role {
    margin: 16px 0 0;
    font-size: 28px;
    color: var(--ink);
  }
  .contact-details {
    list-style: none;
    margin: 58px 0 0;
    padding: 0;
    font-size: 28px;
    line-height: 41px;
    color: var(--ink);
  }
</style>
</head>
<body>
  <main class="card">
    <section class="brand">
      <p class="brand-name">Brett Olsen Building</p>
      <div class="brand-legal">Brett Olsen Building<br>PTY LTD</div>
    </section>

    <div class="divider"></div>

    <section class="contact">
      <h1 class="contact-name">Brett Olsen</h1>
      <p class="contact-role">Director</p>
      <ul class="contact-details">
        <li>A.B.N. 37 829 516 073</li>
        <li>Builders Licence No. 573019k</li>
        <li>M : 0412 907 381</li>
        <li>brettolsenbuilding@mailvane.com.au</li>
      </ul>
    </section>
  </main>
</body>
</html>
```